Building Referrer Relationships Booklet

4 page A4 booklet to give to potential professional referrers to establish a collaborative relationship.Needs to be bright, vibrant, colourful, friendly, inviting, in keeping with The Wren Clinic colours.
Want to provide potential referrer partners a great reason to choose to collaborate with us. They need to know who we are, what makes us different/appealing, and who we are looking for to connect with.
The final product should communicate high performance and connectedness.

Target Market(s)

professional medical allied health and fitness practitioners

Industry/Entity Type

Health

Requirements
Must have
• energetic, vibrant, engaging, inviting, images

```html
<!DOCTYPE html>
<html lang="en">
<head>
<meta charset="utf-8">
<title>Referral Partners Required – The Wren Clinic</title>
<link href="https://fonts.googleapis.com/css2?family=Arimo:wght@400;700&display=swap" rel="stylesheet">
<style>
  :root {
    --orange: #e5500b;
    --orange-bright: #ff6a12;
    --ink: #1c1c1c;
    --white: #ffffff;
    --photo-light: #eef1f4;
    --photo-mid: #cfd6dd;
    --photo-dark: #8fa0b1;
  }
  * { margin: 0; padding: 0; box-sizing: border-box; }
  html, body { width: 1200px; height: 902px; overflow: hidden; }
  body { font-family: "Arimo", Arial, sans-serif; color: var(--ink); background: var(--white); }

  .page { position: relative; width: 1200px; height: 902px; overflow: hidden; }

  .hero-photo {
    position: absolute; inset: 0;
    background:
      radial-gradient(ellipse 260px 420px at 1110px 380px, #e9d3c7 0%, rgba(233,211,199,0) 70%),
      radial-gradient(ellipse 420px 500px at 980px 500px, #b9c6d3 0%, rgba(185,198,211,0) 75%),
      linear-gradient(100deg, var(--photo-light) 0%, var(--photo-mid) 60%, var(--photo-dark) 85%, #c7cfd7 100%);
  }

  .content-veil {
    position: absolute; left: 0; top: 0; width: 716px; height: 902px;
    background: rgba(255,255,255,0.84);
  }

  .section-title {
    position: absolute; left: 0; width: 716px; text-align: center;
    color: var(--orange); font-size: 20px; font-weight: 700; letter-spacing: 0.2px;
  }

  .partner {
    position: absolute; left: 24px; width: 680px;
  }
  .partner::before {
    content: ""; position: absolute; left: 0; top: -3px;
    width: 34px; height: 38px; background: var(--orange);
  }
  .partner h3 { margin-left: 45px; font-size: 15px; font-weight: 700; line-height: 19px; }
  .partner p { margin-left: 45px; font-size: 15px; line-height: 20px; }

  .partner-strip {
    position: absolute; left: -20px; top: 800px; width: 736px; height: 90px;
    background: var(--white); border-radius: 0 14px 14px 0;
    box-shadow: 0 -2px 10px rgba(0,0,0,0.15);
  }
  .partner-badge { position: absolute; top: 20px; height: 54px; }

  .feature-rule {
    position: absolute; left: 738px; width: 432px; height: 5px; background: var(--white);
    box-shadow: 0 1px 3px rgba(0,0,0,0.15);
  }
  .feature-title {
    position: absolute; left: 775px; top: 585px; width: 400px;
    color: var(--orange-bright); font-size: 69px; font-weight: 700; line-height: 65px;
    text-shadow: 0 1px 2px rgba(0,0,0,0.15);
  }
</style>
</head>
<body>
<main class="page">
  <div class="hero-photo" role="img" aria-label="Soft-focus photo of a doctor in a white coat with a stethoscope giving two thumbs up"></div>
  <div class="content-veil"></div>

  <h2 class="section-title" style="top:74px">REFERRAL PARTNERS REQUIRED</h2>

  <div class="partner" style="top:120px"><h3>MASSAGE THERAPISTS</h3><p>Deep tissue and remedial massage Therapeutic massage</p></div>
  <div class="partner" style="top:179px"><h3>FASCIAL THERAPISTS</h3><p>Kinetic Line fascial releases to reset the alignment of the whole body</p></div>
  <div class="partner" style="top:239px"><h3>PHYSIOTHERAPISTS</h3><p>Pain relief, protect and strengthen both lower limb and upper limb</p></div>
  <div class="partner" style="top:298px"><h3>GP, SPORTS PHYSICIANS</h3><p>General health, diagnostics, treatment support, prescription medications</p></div>

  <h2 class="section-title" style="top:357px">SPECIALIST REFERRALS</h2>

  <div class="partner" style="top:403px"><h3>OSTEOPATHS AND CHIROPRACTORS</h3><p>Mobilisations and manipulative therapy for the spinal column and limbs</p></div>
  <div class="partner" style="top:463px"><h3>DIETICIAN AND NUTRITIONISTS</h3><p>DEXA scan for bone density/lean mass/fat mass<br>Optimising gut health and nutrition - You are what you eat!</p></div>
  <div class="partner" style="top:542px"><h3>PSYCHOLOGISTS/PSYCHIATRISTS</h3><p>Sometimes our physical body cannot get better until we optimise a healthy mind</p></div>
  <div class="partner" style="top:602px"><h3>PERSONAL TRAINERS, PILATES AND YOGA INSTRUCTORS</h3><p>Create awesome body strength, flexibility and resilience</p></div>
  <div class="partner" style="top:661px"><h3>SURGEONS</h3><p>When conservative methods are ineffective, surgical intervention works well.</p></div>

  <div class="partner-strip">
    <svg class="partner-badge" style="left:36px" width="170" height="54" aria-hidden="true"><rect width="170" height="54" rx="3" fill="#d9232e" opacity="0.85"/></svg>
    <svg class="partner-badge" style="left:225px" width="95" height="54" aria-hidden="true"><rect width="95" height="54" rx="3" fill="#1a62b5"/></svg>
    <svg class="partner-badge" style="left:340px" width="150" height="54" aria-hidden="true"><rect width="150" height="54" rx="3" fill="#c9c9c9"/></svg>
    <svg class="partner-badge" style="left:500px" width="160" height="54" aria-hidden="true"><rect width="160" height="54" rx="3" fill="#244a9c"/></svg>
  </div>

  <div class="feature-rule" style="top:532px"></div>
  <h1 class="feature-title">REFERRAL PARTNERS REQUIRED</h1>
  <div class="feature-rule" style="top:806px"></div>
</main>
</body>
</html>
```